Criação de Folder para Tecnologia & Ciencias
A empresa queria:
" A Quitafor é uma empresa que desenvolve e fornece o sistema de cobrança Quitafor para empresas de cobrança (escritórios de cobrança, assessorias de cobranças, escritórios de advogados), tais clientes chamamos de ASSESSORIAS, e também fornecemos o sistema para empresas que possuem uma grande quantidade de clientes inadimplentes e que fazem a cobrança destes clientes internamente através de um departamento de cobrança, estes clientes chamamos de CREDORES. Alguns clientes ASSESSORIAS: www.grupoltv.com.br www.dornelesmota.com.br www.rixamonte.com.br Alguns clientes CREDORES: www.brightlane.com www.grupovelarim.com.br www.tadeus.com.br Todos os produtos e serviços que comercializamos são através da plataforma Quitafor, por exemplo, para que um cliente utilize nosso produto “Painel de Acordos” ele precisa contratar o Quitafor já que suas configurações são através do sistema, da mesma forma o serviço de “SMS”, já que as campanhas são criadas e disparadas pelo sistema Quitafor. O sistema Quitafor “nasceu” primeiro que a empresa Quitafor, já que dois dos atuais sócios possuíram uma empresa anterior de 2012 até a abertura da Quitafor em 1 de setembro de 2015. Esta empresa desenvolvia um sistema focado para assessorias de cobrança, porém em uma tecnologia antiga, e então resolveram criar um novo software com tecnologias atuais na época e para isto buscaram um investidor e juntos optaram por criar uma nova empresa, uma nova marca. Nossa logo foi construída através da plataforma Marca Pronta e gostamos muito do resultado! E estamos aqui novamente buscando que seus profissionais nos ajudem a criar novos materiais que hoje se fazem necessários para nós. "

```html
<!DOCTYPE html>
<html lang="pt-BR">
<head>
<meta charset="UTF-8">
<title>Quitafor – Folder</title>
<link href="https://fonts.googleapis.com/css2?family=Montserrat:wght@300;400;500;600;700;800&display=swap" rel="stylesheet">
<style>
  :root{
    --bg:#ecebe7;
    --blue:#1f3fae;
    --blue-dark:#15308c;
    --white:#ffffff;
    --paper:#f3f4f7;
    --ink:#4a4f5c;
    --photo-a:#c9d3e6;
    --photo-b:#6f7f9e;
  }
  *{box-sizing:border-box;margin:0;padding:0}
  html,body{width:1200px;height:1200px;overflow:hidden;background:var(--bg);font-family:'Montserrat',sans-serif}
  .brochure{position:absolute;left:30px;top:310px;width:1140px;height:580px;display:flex;box-shadow:0 10px 30px rgba(0,0,0,.18)}
  .panel{width:380px;height:100%;position:relative;overflow:hidden}

  /* inside panel */
  .panel--about{background:var(--paper)}
  .about-photo{height:200px;background:linear-gradient(135deg,var(--photo-a),var(--photo-b))}
  .about-tag{position:absolute;left:120px;top:184px;width:140px;height:32px;background:var(--blue);color:var(--white);font-weight:700;font-size:14px;display:flex;align-items:center;justify-content:center}
  .about-text{padding:34px 28px 0;font-size:9.5px;line-height:1.6;color:var(--ink);text-align:justify}
  .numbers-title{margin:20px 0 12px;text-align:center;color:var(--blue);font-weight:700;font-size:16px}
  .numbers{display:flex;gap:12px;padding:0 22px}
  .numbers-list{flex:1;list-style:none}
  .numbers-list li{display:flex;align-items:center;justify-content:flex-end;gap:6px;font-size:9px;color:var(--ink);font-weight:500;height:27px}
  .tick{width:14px;height:14px;flex:none}
  .numbers-boxes{width:150px;display:flex;flex-direction:column;gap:10px}
  .stat{background:var(--blue);color:var(--white);padding:6px 8px;text-align:center}
  .stat strong{display:block;font-size:15px;font-weight:800}
  .stat span{font-size:8.5px;font-weight:500}

  /* contact panel */
  .panel--contact{background:var(--blue)}
  .brand-band{position:absolute;left:0;top:210px;width:100%;height:80px;background:var(--white);display:flex;align-items:center;justify-content:center}
  .brand-band .brand{color:var(--blue);font-size:40px;font-weight:700;letter-spacing:-.5px}
  .contact{position:absolute;left:40px;top:340px;color:var(--white)}
  .contact h2{font-size:15px;font-weight:700;margin-bottom:16px}
  .contact ul{list-style:none}
  .contact li{display:flex;align-items:center;gap:10px;font-size:11px;margin-bottom:12px}
  .contact svg{width:16px;height:16px;flex:none}

  /* cover panel */
  .panel--cover{background:var(--blue-dark)}
  .slogan-frame{position:absolute;left:30px;top:60px;width:310px;height:260px;border:1.5px solid var(--white)}
  .slogan{position:absolute;right:50px;top:80px;text-align:right;color:var(--white);font-size:17px;line-height:1.3;text-transform:uppercase;font-weight:300}
  .slogan b{font-weight:800}
  .cover-brand{position:absolute;right:40px;top:345px;text-align:right;color:var(--white)}
  .cover-brand .brand{font-size:34px;font-weight:700;letter-spacing:-.5px}
  .cover-brand small{display:block;font-size:8px;letter-spacing:2px;text-transform:uppercase;font-weight:400}
</style>
</head>
<body>
<main class="brochure">
  <section class="panel panel--about">
    <div class="about-photo" role="img" aria-label="Foto de equipe reunida em escritório"></div>
    <div class="about-tag">Sobre Nós</div>
    <p class="about-text">A Quitafor desenvolve soluções de cobrança desde 2015, unindo tecnologia atual e experiência de mercado. Atendemos assessorias, escritórios de advocacia e credores com departamentos próprios de cobrança, oferecendo uma plataforma completa para gestão de carteiras, acordos, campanhas de SMS e relatórios. Nosso foco é gerar resultados reais para cada cliente.</p>
    <h2 class="numbers-title">Nossos Números</h2>
    <div class="numbers">
      <ul class="numbers-list">
        <li>+ de 30 assessorias <svg class="tick" viewBox="0 0 16 16"><circle cx="8" cy="8" r="8" fill="#1f3fae"/><path d="M4.5 8.2l2.3 2.3 4.7-4.8" stroke="#fff" stroke-width="1.8" fill="none"/></svg></li>
        <li>+ de 20 credores <svg class="tick" viewBox="0 0 16 16"><circle cx="8" cy="8" r="8" fill="#1f3fae"/><path d="M4.5 8.2l2.3 2.3 4.7-4.8" stroke="#fff" stroke-width="1.8" fill="none"/></svg></li>
        <li>+ de 2000 usuários <svg class="tick" viewBox="0 0 16 16"><circle cx="8" cy="8" r="8" fill="#1f3fae"/><path d="M4.5 8.2l2.3 2.3 4.7-4.8" stroke="#fff" stroke-width="1.8" fill="none"/></svg></li>
        <li>50 integrações ativas <svg class="tick" viewBox="0 0 16 16"><circle cx="8" cy="8" r="8" fill="#1f3fae"/><path d="M4.5 8.2l2.3 2.3 4.7-4.8" stroke="#fff" stroke-width="1.8" fill="none"/></svg></li>
        <li>100% em nuvem segura <svg class="tick" viewBox="0 0 16 16"><circle cx="8" cy="8" r="8" fill="#1f3fae"/><path d="M4.5 8.2l2.3 2.3 4.7-4.8" stroke="#fff" stroke-width="1.8" fill="none"/></svg></li>
        <li>+ de 5000 acordos diários <svg class="tick" viewBox="0 0 16 16"><circle cx="8" cy="8" r="8" fill="#1f3fae"/><path d="M4.5 8.2l2.3 2.3 4.7-4.8" stroke="#fff" stroke-width="1.8" fill="none"/></svg></li>
      </ul>
      <div class="numbers-boxes">
        <div class="stat"><strong>+ de 1 milhão</strong><span>de acordos por ano</span></div>
        <div class="stat"><strong>+ de 700 milhões</strong><span>em valores recuperados</span></div>
        <div class="stat"><strong>+ de 30 milhões</strong><span>de SMS enviados</span></div>
      </div>
    </div>
  </section>

  <section class="panel panel--contact">
    <div class="brand-band"><span class="brand">quitafor</span></div>
    <div class="contact">
      <h2>Fale Conosco</h2>
      <ul>
        <li><svg viewBox="0 0 16 16"><path d="M4 1.5l2.5 3-1.5 1.8c.8 1.8 2 3 3.8 3.8L10.6 8.6l3 2.5-1.3 2.6C7 13.5 2.5 9 2.3 3.4z" fill="#fff"/></svg>(11) 4020-1180 | (11) 98765-4321</li>
        <li><svg viewBox="0 0 16 16"><rect x="1.5" y="3.5" width="13" height="9" fill="none" stroke="#fff" stroke-width="1.4"/><path d="M1.5 3.5L8 9l6.5-5.5" fill="none" stroke="#fff" stroke-width="1.4"/></svg>contato@quitafor.com.br</li>
        <li><svg viewBox="0 0 16 16"><circle cx="8" cy="8" r="6.3" fill="none" stroke="#fff" stroke-width="1.4"/><ellipse cx="8" cy="8" rx="2.8" ry="6.3" fill="none" stroke="#fff" stroke-width="1.2"/><path d="M1.7 8h12.6" stroke="#fff" stroke-width="1.2"/></svg>www.quitafor.com.br</li>
        <li><svg viewBox="0 0 16 16"><path d="M8 15s5-5.2 5-8.8A5 5 0 0 0 3 6.2C3 9.8 8 15 8 15z" fill="#fff"/><circle cx="8" cy="6.2" r="1.8" fill="#1f3fae"/></svg>Av. Paulista Central, 500 - São Paulo/SP</li>
      </ul>
    </div>
  </section>

  <section class="panel panel--cover">
    <div class="slogan-frame"></div>
    <p class="slogan">Nós desenvolvemos<br><b>tecnologias</b><br>que geram mais<br><b>resultados</b> para<br><b>empresas</b> e<br><b>departamentos</b><br>de <b>cobrança</b></p>
    <div class="cover-brand"><span class="brand">quitafor</span><small>Sistema de cobrança</small></div>
  </section>
</main>
</body>
</html>
```